Corporate Design für Onlineshop zum Verkauf von asiatischen Reflexbögen
Ein tolles Design und hervorragende Zusammenarbeit! Alle unsere Sonderwünsche wurden einwandfrei umgesetzt. Ich kann Vrelmo aus vollstem Herzen empfehlen. Unser Gewinner!
Zielgruppe
Ich bin Einzelunternehmer (Marwend Bogensport Helmut Drabeck) und verkaufe in meinem Webshop Asiatische Reflexbögen, häufig auch als Reiterbögen bezeichnet, und alles was der traditionelle Bogenschütze so braucht (z.B. Pfeile, Köcher, Zubehör, etc...)
Aufgabenstellung
Ich suche ein einprägsames Design, das in verschiedenen Größen gut funktioniert und erkennbar ist (sowohl als kleines Logo als auch größer auf Messeständen oder Flyern).
Das Logo sollte am Besten sowohl farbig (z.B. Onlineshop, Visitenkarte, Briefkopf) als auch schwarz/weiß (z.B. als Gravur auf Leder oder Holz) funktionieren.
Wenn die Silouhette eines gespannten typischen Reiterbogens (tatarisch, mongolisch, skytisch oder chinesisch) im Logo drin wäre und ein stilisierter Fuchs, dann würde das den Namen villeicht ganz gut untermalen glaub ich.
Meine Hauptkunden sind Bogenschützen, die vornehmlich mit traditionellen Bögen schießen, sowohl auf dem Platz als auch in der Natur auf dem 3D-Parcours.
Der Name MarWend leitet sich von 'fux = Fuchs' und 'luoga = versteckter Wohnung' ab, heißt also in etwa 'Fuchsbau' so sind hier im Süddeutschen und Österreichischen einige Ortsteile bzw. Einöden benannt, z.B. Marwend oder Fuchslug in Aschau im Chiemgau.
Meinen Onlineshop baue ich gerade auf, da ist also noch nicht wirklich was zu sehen. Ich brauche daher ein Logo für Shop, Visitenkarte und Briefpapier und ein Design für Visitenkarte und ein Design für Briefpapier/Rechnungen.

```html
<!DOCTYPE html>
<html lang="en">
<head>
<meta charset="utf-8">
<title>Marwend Bogensport – Corporate Design</title>
<link rel="stylesheet" href="https://fonts.googleapis.com/css2?family=Montserrat:wght@600;700;800&family=PT+Sans:wght@400;700&display=swap">
<style>
  :root{
    --bg:#333333;
    --paper:#f6f6f4;
    --white:#ffffff;
    --green:#009140;
    --orange:#f39c00;
  }
  *{box-sizing:border-box;margin:0;padding:0}
  html,body{width:1200px;height:1200px;overflow:hidden;background:var(--bg)}
  .canvas{position:relative;width:1200px;height:1200px;background:var(--bg);font-family:"PT Sans",sans-serif}

  .rule{position:absolute;height:6px;background:var(--white)}
  .rule--top{left:0;top:200px;width:820px}
  .rule--bottom{left:200px;top:1059px;width:1000px}

  .showcase{position:absolute;border-radius:50%;background:var(--white);border:10px solid var(--bg);box-shadow:0 0 0 6px var(--white);display:flex;align-items:center;justify-content:center;overflow:hidden}
  .showcase--logo{left:819px;top:51px;width:304px;height:304px}
  .showcase--mark{left:37px;top:980px;width:164px;height:164px}

  .wordmark{font-family:"Montserrat",sans-serif;font-weight:800;color:var(--green);letter-spacing:.5px;display:flex;align-items:center;gap:8px;line-height:1;white-space:nowrap}
  .wordmark__dot{border-radius:50%;border:3px solid var(--orange);background:var(--white);flex:none}
  .wordmark--hero{font-size:36px;margin-top:40px}
  .wordmark--hero .wordmark__dot{width:20px;height:20px}
  .wordmark--small{font-size:19px}

  .sheet{position:absolute;background:var(--paper);box-shadow:0 18px 30px rgba(0,0,0,.45);overflow:hidden}
  .band{position:absolute;left:0;right:0;background:
     linear-gradient(180deg,var(--green) 0 58%,var(--white) 58% 66%,var(--orange) 66% 82%,var(--white) 82% 100%)}
  .band--flip{background:
     linear-gradient(0deg,var(--green) 0 58%,var(--white) 58% 66%,var(--orange) 66% 82%,var(--white) 82% 100%)}

  .letterhead{left:60px;top:250px;width:460px;height:650px}
  .letterhead .band{height:26px}
  .letterhead .band--top{top:0}
  .letterhead .band--bottom{bottom:0}
  .letterhead__logo{position:absolute;left:38px;top:50px}
  .letterhead__logo .wordmark{font-size:26px}
  .letterhead__logo .wordmark__dot{width:16px;height:16px;border-width:2px}
  .letterhead__body{position:absolute;left:38px;right:38px;top:102px;color:var(--green);font-size:9.4px;line-height:1.42}
  .letterhead__body h2{font-family:"Montserrat",sans-serif;font-size:13px;font-weight:700;margin-bottom:6px}
  .letterhead__body p{margin-bottom:7px}
  .letterhead__contact{position:absolute;left:38px;bottom:50px;color:var(--green);font-size:7.4px;letter-spacing:.8px;text-transform:uppercase;line-height:1.6}
  .signature{width:90px;height:22px;border-bottom:1px solid var(--green);margin-bottom:3px}
  .signature__name{font-size:6px;letter-spacing:1.4px;margin-bottom:10px}
  .contact-row{display:flex;align-items:center;gap:5px;text-transform:none}
  .contact-row svg{width:8px;height:8px;flex:none}

  .envelope{left:560px;top:410px;width:380px;height:180px}
  .envelope .stripe{position:absolute;top:0;bottom:0;right:0;width:30px;background:
     linear-gradient(270deg,var(--green) 0 58%,var(--white) 58% 66%,var(--orange) 66% 82%,var(--white) 82% 100%)}
  .envelope__logo{position:absolute;left:22px;bottom:20px}
  .envelope__logo .wordmark{font-size:17px}
  .envelope__logo .wordmark__dot{width:12px;height:12px;border-width:2px}

  .card{width:280px;height:172px;top:640px}
  .card--front{left:560px}
  .card--back{left:860px}
  .card--front .band{height:40px}
  .card--front .band--top{top:0}
  .card--front .band--bottom{bottom:0}
  .card__logo{position:absolute;left:0;right:0;top:72px;display:flex;justify-content:center}
  .card__logo .wordmark{font-size:22px}
  .card__logo .wordmark__dot{width:15px;height:15px;border-width:2px}

  .card--back .band{height:22px}
  .card--back .band--top{top:0}
  .card--back .band--bottom{bottom:0}
  .card__name{position:absolute;left:20px;top:36px;font-family:"Montserrat",sans-serif;font-weight:800;font-size:15px;color:var(--green);border-bottom:1.5px solid var(--green);padding-bottom:2px}
  .card__position{position:absolute;left:92px;top:58px;font-family:"Montserrat",sans-serif;font-weight:600;font-size:6px;letter-spacing:2px;color:var(--orange)}
  .card__web{position:absolute;left:20px;top:80px;font-size:7.5px;color:var(--green);font-weight:700}
  .card__backlogo{position:absolute;right:20px;top:86px}
  .card__backlogo .wordmark{font-size:17px}
  .card__backlogo .wordmark__dot{width:11px;height:11px;border-width:2px}
  .card__footer{position:absolute;left:20px;right:20px;bottom:30px;display:flex;justify-content:space-between;font-size:7.5px;color:var(--green);font-weight:700}
</style>
</head>
<body>
<main class="canvas">
  <div class="rule rule--top"></div>
  <div class="rule rule--bottom"></div>

  <section class="showcase showcase--logo">
    <div class="wordmark wordmark--hero">MARWEND<span class="wordmark__dot"></span></div>
  </section>

  <section class="showcase showcase--mark">
    <div class="wordmark wordmark--small">MARWEND</div>
  </section>

  <article class="sheet letterhead">
    <div class="band band--top"></div>
    <div class="letterhead__logo"><div class="wordmark">MARWEND<span class="wordmark__dot"></span></div></div>
    <div class="letterhead__body">
      <h2>Branding</h2>
      <p>Branding is defined as the process of coming up or making a unique name or design for a certain product.</p>
      <p>Having a good brand strategy allows you to have a major advantage in gaining a large increase in your market competitions. Your brand tells your customers what they can expect from the products and services you offer.</p>
      <p>Are you innovative or are you the experienced type? Do you offer a high-cost, high-quality product, or a low-cost, high-value product? It's impossible to be both. You should consider thinking what your customers need you to be. Your logo is the main foundation of your brand. All the promotional materials should be connected with your logo to communicate with your brand.</p>
      <p>Brand messages are delivered and planned based on the questions how, what, when, to whom and where your brand strategy is. Advertisement, visual communication, and distribution channels are parts of brand strategy.</p>
      <p>The branding strategy you have should be consistent as it leads to a strong brand equity.</p>
    </div>
    <div class="letterhead__contact">
      <div class="signature"></div>
      <div class="signature__name">Name Surname</div>
      <div>1234 Your Location Here</div>
      <div>Your Rd. Your Street</div>
      <div>Postal 0000</div>
      <div class="contact-row"><svg viewBox="0 0 10 10"><path d="M2 1l2 0 1 2.5-1.3 1a5 5 0 0 0 2.8 2.8l1-1.3L10 7v2c0 .6-.4 1-1 1A9 9 0 0 1 0 1c0-.6.4-1 1-1z" fill="var(--orange)"/></svg>123-4567-890</div>
      <div class="contact-row"><svg viewBox="0 0 10 10"><circle cx="5" cy="5" r="4.5" fill="var(--orange)"/></svg>www.MarWend.com</div>
      <div class="contact-row"><svg viewBox="0 0 10 10"><circle cx="5" cy="5" r="4.5" fill="var(--orange)"/></svg>www.MarWend.de</div>
    </div>
    <div class="band band--flip band--bottom"></div>
  </article>

  <article class="sheet envelope">
    <div class="envelope__logo"><div class="wordmark"><span class="wordmark__dot"></span>MARWEND</div></div>
    <div class="stripe"></div>
  </article>

  <article class="sheet card card--front">
    <div class="band band--top"></div>
    <div class="card__logo"><div class="wordmark">MARWEND<span class="wordmark__dot"></span></div></div>
    <div class="band band--flip band--bottom"></div>
  </article>

  <article class="sheet card card--back">
    <div class="band band--top"></div>
    <div class="card__name">YOUR NAME</div>
    <div class="card__position">POSITION</div>
    <div class="card__web">www.MarWend.de</div>
    <div class="card__backlogo"><div class="wordmark">MARWEND<span class="wordmark__dot"></span></div></div>
    <div class="card__footer">
      <span class="contact-row"><svg viewBox="0 0 10 10"><path d="M2 1l2 0 1 2.5-1.3 1a5 5 0 0 0 2.8 2.8l1-1.3L10 7v2c0 .6-.4 1-1 1A9 9 0 0 1 0 1c0-.6.4-1 1-1z" fill="var(--green)"/></svg>123-4567-890</span>
      <span class="contact-row"><svg viewBox="0 0 10 10"><circle cx="5" cy="5" r="4.5" fill="var(--orange)"/></svg>www.MarWend.com</span>
    </div>
    <div class="band band--flip band--bottom"></div>
  </article>
</main>
</body>
</html>
```